Bluefern painting and decorating *

Need a flyer design to advertise my services
So the information I need included is the services we offer at bluefern painting and decorating which include
Interior painting
Exterior painting
Wallpaper hanging
Paint and cellulose spraying
Dust free sanding
Pressure washing
Stone cleaning
Also would need to have my company contact details in
Www.bluefernpaintingdecorating.co.uk
Email is info@bluefernpaintingdecorating.com
Bluefern Painting & Decorating Services has a proven track record of innovative designs, effective problem solving and attention to detail and our goal is to meet and exceed the expectations of every customer. We take on all types of jobs from small domestic work to larger commercial projects, all carried out to the highest standards, and at very competitive prices.

```html
<!DOCTYPE html>
<html lang="en">
<head>
<meta charset="utf-8">
<title>Bluefern Painting and Decorating – Flyer</title>
<link href="https://fonts.googleapis.com/css2?family=Oswald:wght@500&family=Roboto+Condensed:wght@400;700&family=Libre+Baskerville&display=swap" rel="stylesheet">
<style>
  :root {
    --royal: #3a3f9c;
    --royal-deep: #2e3384;
    --navy: #14406f;
    --gold: #d9a31e;
    --gold-light: #f0cf6a;
    --paper: #f3f3f3;
    --white: #ffffff;
    --ink: #1d2a4a;
  }
  * { margin: 0; padding: 0; box-sizing: border-box; }
  html, body { width: 896px; height: 1200px; overflow: hidden; background: #e9e9e9; }
  .flyer { position: relative; width: 896px; height: 1200px; overflow: hidden; background: var(--paper); }
  .backdrop { position: absolute; inset: 0; }
  .hero-photo { position: absolute; left: 0; top: 0; width: 896px; height: 490px;
    background: linear-gradient(160deg, #d8d4cf 0%, #b9b3ab 30%, #ece9e6 55%, #c49a6c 80%, #a7774c 100%); }
  .detail-photo { position: absolute; border-radius: 50%; border: 4px solid var(--white);
    box-shadow: 0 0 0 5px var(--gold), 0 4px 10px rgba(0,0,0,.25); }
  .detail-photo.floor { left: 28px; top: 410px; width: 240px; height: 240px;
    background: linear-gradient(170deg, #cfd1d3 0%, #8e9194 45%, #dfe1e2 100%); }
  .detail-photo.fireplace { left: 288px; top: 450px; width: 196px; height: 196px;
    background: linear-gradient(180deg, #b9b5ae 0%, #e8e6e2 55%, #8f8b86 100%); }

  .services { position: absolute; left: 24px; top: 672px; color: var(--white); }
  .services h2 { font: 500 30px/1 "Oswald", sans-serif; letter-spacing: -0.3px; margin-bottom: 36px; }
  .service-list { list-style: none; }
  .service { display: flex; align-items: center; height: 61px;
    font: 500 24px/1 "Oswald", sans-serif; letter-spacing: 0.2px; }
  .service-icon { width: 54px; height: 54px; border: 2px solid var(--white); border-radius: 50%;
    margin-right: 16px; display: flex; align-items: center; justify-content: center; }

  .brand { position: absolute; right: 24px; top: 550px; text-align: center; color: var(--navy);
    font-family: "Roboto Condensed", sans-serif; font-weight: 700; }
  .brand-name { font-size: 62px; line-height: 1; letter-spacing: 2px; }
  .brand-line { font-size: 17px; letter-spacing: 1.4px; margin-top: 2px; }
  .brand-rule { height: 2px; background: var(--navy); margin-top: 12px; }

  .headline { position: absolute; right: 24px; top: 686px; text-align: right; color: var(--gold);
    font: 400 47px/1.08 "Libre Baskerville", serif; }
  .about { position: absolute; right: 24px; top: 805px; width: 420px; text-align: right;
    color: var(--ink); font: 400 17.5px/24px "Roboto Condensed", sans-serif; letter-spacing: -0.3px; }

  .contact { position: absolute; right: 24px; top: 1030px; text-align: right; }
  .contact h3 { font: 500 31px/1 "Oswald", sans-serif; color: var(--gold); margin-bottom: 8px; }
  .contact-line { display: flex; justify-content: flex-end; align-items: center; height: 37px;
    font: 700 22px/1 "Roboto Condensed", sans-serif; color: var(--navy); letter-spacing: -0.3px; }
  .contact-line.phone { font: 500 25px/1 "Oswald", sans-serif; }
  .contact-icon { width: 28px; height: 28px; border-radius: 50%; background: var(--gold);
    border: 2px solid var(--gold-light); margin-left: 10px; display: flex; align-items: center; justify-content: center; }
</style>
</head>
<body>
<main class="flyer">
  <div class="hero-photo" role="img" aria-label="Photo of a bright open-plan living room with a white sofa, dining table and tiled kitchen wall"></div>

  <svg class="backdrop" width="896" height="1200" viewBox="0 0 896 1200" aria-hidden="true">
    <path d="M0,486 Q420,540 896,458 L896,1200 L0,1200 Z" fill="var(--paper)"/>
    <path d="M0,486 Q420,540 896,458" fill="none" stroke="var(--gold)" stroke-width="4"/>
    <path d="M0,494 Q200,500 352,580 C420,720 450,920 450,1200 L0,1200 Z" fill="var(--royal)"/>
    <path d="M362,600 C428,740 460,930 458,1200" fill="none" stroke="var(--white)" stroke-width="10"/>
    <path d="M356,590 C424,732 456,925 455,1200" fill="none" stroke="var(--gold)" stroke-width="6"/>
    <path d="M0,1200 L0,1120 Q200,1180 440,1140 L440,1200 Z" fill="var(--royal-deep)" opacity="0.5"/>
  </svg>

  <div class="detail-photo floor" role="img" aria-label="Photo of a freshly painted glossy grey floor"></div>
  <div class="detail-photo fireplace" role="img" aria-label="Photo of a decorated room with a white fireplace surround"></div>

  <section class="services">
    <h2>SERVICES WE OFFER INCLUDE...</h2>
    <ul class="service-list">
      <li class="service"><span class="service-icon"><svg width="30" height="30" viewBox="0 0 30 30"><rect x="4" y="4" width="20" height="8" rx="2" fill="var(--gold)"/><path d="M24,8 H27 V16 H15 V19" fill="none" stroke="var(--gold)" stroke-width="2"/><rect x="13" y="19" width="4" height="9" rx="1" fill="var(--gold)"/></svg></span>INTERIOR PAINTING</li>
      <li class="service"><span class="service-icon"><svg width="30" height="30" viewBox="0 0 30 30"><rect x="3" y="12" width="10" height="15" fill="var(--gold)"/><rect x="14" y="4" width="12" height="23" fill="var(--gold)"/><path d="M17,8 h6 M17,13 h6 M17,18 h6 M5,16 h6 M5,21 h6" stroke="var(--royal)" stroke-width="2"/></svg></span>EXTERIOR PAINTING</li>
      <li class="service"><span class="service-icon"><svg width="30" height="30" viewBox="0 0 30 30"><rect x="3" y="5" width="24" height="20" rx="2" fill="var(--gold)"/><path d="M5,22 L12,14 L17,19 L21,15 L25,22 Z" fill="var(--royal)"/><circle cx="21" cy="10" r="2.5" fill="var(--royal)"/></svg></span>WALLPAPER HANGING</li>
      <li class="service"><span class="service-icon"><svg width="30" height="30" viewBox="0 0 30 30"><rect x="10" y="11" width="10" height="17" rx="2" fill="var(--gold)"/><rect x="12" y="6" width="6" height="5" fill="var(--gold)"/><circle cx="7" cy="5" r="1.3" fill="var(--gold)"/><circle cx="5" cy="9" r="1.3" fill="var(--gold)"/></svg></span>PAINT &amp; CELLULOSE SPRAYING</li>
      <li class="service"><span class="service-icon"><svg width="30" height="30" viewBox="0 0 30 30"><circle cx="15" cy="15" r="8" fill="var(--gold)"/><circle cx="5" cy="7" r="2.5" fill="var(--gold)"/><circle cx="25" cy="8" r="2" fill="var(--gold)"/><circle cx="24" cy="24" r="2.5" fill="var(--gold)"/><circle cx="6" cy="23" r="2" fill="var(--gold)"/></svg></span>DUST FREE SANDING</li>
      <li class="service"><span class="service-icon"><svg width="30" height="30" viewBox="0 0 30 30"><path d="M4,27 L18,13" stroke="var(--gold)" stroke-width="3"/><rect x="16" y="9" width="6" height="6" transform="rotate(45 19 12)" fill="var(--gold)"/><path d="M22,8 L27,3 M23,10 L28,7 M20,6 L24,2" stroke="var(--gold)" stroke-width="1.5"/></svg></span>PRESSURE WASHING</li>
      <li class="service"><span class="service-icon"><svg width="30" height="30" viewBox="0 0 30 30"><g fill="var(--gold)"><rect x="12" y="3" width="6" height="6" transform="rotate(45 15 6)"/><rect x="6" y="9" width="6" height="6" transform="rotate(45 9 12)"/><rect x="18" y="9" width="6" height="6" transform="rotate(45 21 12)"/><rect x="12" y="15" width="6" height="6" transform="rotate(45 15 18)"/><rect x="6" y="21" width="6" height="6" transform="rotate(45 9 24)" opacity=".8"/><rect x="18" y="21" width="6" height="6" transform="rotate(45 21 24)" opacity=".8"/></g></svg></span>STONE CLEANING</li>
    </ul>
  </section>

  <header class="brand">
    <div class="brand-name">BLUEFERN</div>
    <div class="brand-line">PAINTING AND DECORATING SERVICES</div>
    <div class="brand-rule"></div>
  </header>

  <h1 class="headline">PAINTING &amp;<br>DECORATING</h1>

  <p class="about">Bluefern Painting &amp; Decorating Services has a proven track record of innovative designs, effective problem solving and attention to detail and our goal is to meet and exceed the expectations of every customer. We take on all types of jobs from small domestic work to larger commercial projects, all carried out to the highest standards, and at very competitive prices.</p>

  <section class="contact">
    <h3>CALL FOR A FREE QUOTE</h3>
    <div class="contact-line phone">07700 900 418<span class="contact-icon"><svg width="16" height="16" viewBox="0 0 16 16"><path d="M3,2 L6,2 L7,5 L5.5,6.5 Q7,9.5 9.5,10.5 L11,9 L14,10 L14,13 Q8,14 3,8 Q2,5 3,2 Z" fill="var(--white)"/></svg></span></div>
    <div class="contact-line">www.bluefernpaintingdecorating.co.uk<span class="contact-icon"><svg width="16" height="16" viewBox="0 0 16 16"><circle cx="8" cy="8" r="6" fill="none" stroke="var(--white)" stroke-width="1.5"/><path d="M2,8 H14 M8,2 Q4,8 8,14 Q12,8 8,2" fill="none" stroke="var(--white)" stroke-width="1.2"/></svg></span></div>
    <div class="contact-line">info@bluefernpaintingdecorating.com<span class="contact-icon"><svg width="16" height="16" viewBox="0 0 16 16"><rect x="2" y="4" width="12" height="8" fill="none" stroke="var(--white)" stroke-width="1.5"/><path d="M2,4 L8,9 L14,4" fill="none" stroke="var(--white)" stroke-width="1.5"/></svg></span></div>
  </section>
</main>
</body>
</html>
```